Harbourlight Dental Centre Kelvale business cards and presentation folder

dental practice needing innovative black business cards for 2 different dentists witrh appointment details written at the back of the card for the patient.
name of dentists: Dr Anjali R Venkatesan B.D.S., M.P.H (Melb)
Dr. Raj Kalpat B.D.S.

Target Market(s)

professioinal, working class

Industry/Entity Type

Dental Clinic

Contact Information for Business Card

Dr. Raj Kalpat B.D.S.

Font styles to use
Sans Serif

Requirements
Must have
• Front side: logo
• dentist name
• phone number: 07- 5918 2243
• back side: appointment details: date, time,
• Address: 117C, 58 Tarrow Street, Kelvale - 4561, Queensland
• Email: admin@harbourlightdentalkelvale.example.au
• Website: www.harbourlightdental.example.au
• preferable logo colors
Nice to have
• classy look more pleasing

```html
<!DOCTYPE html>
<html lang="en">
<head>
<meta charset="utf-8">
<title>Harbourlight Dental Centre Kelvale – Business Card</title>
<link rel="stylesheet" href="https://fonts.googleapis.com/css2?family=Questrial&family=Montserrat:wght@400;600&display=swap">
<style>
  :root {
    --page-bg: #e6e6e6;
    --card-black: #231f20;
    --card-edge: #141213;
    --card-white: #ffffff;
    --brand-green: #9cc36a;
    --text-grey: #b8b8b8;
    --ink: #1d1d1d;
    --rule: #8a8a8a;
  }
  * { box-sizing: border-box; margin: 0; padding: 0; }
  html, body { width: 1200px; height: 1199px; overflow: hidden; }
  body {
    background: var(--page-bg);
    font-family: "Questrial", "Montserrat", sans-serif;
    position: relative;
  }
  .card {
    position: absolute;
    left: 160px;
    width: 880px;
    height: 538px;
    box-shadow: 0 6px 18px rgba(0,0,0,0.18);
  }
  /* Front */
  .card-front {
    top: 40px;
    background: var(--card-black);
    border: 22px solid var(--card-edge);
  }
  .front-brand {
    position: absolute;
    left: 60px;
    top: 70px;
    display: flex;
    align-items: center;
    gap: 16px;
  }
  .brand-dot {
    width: 18px; height: 18px;
    border-radius: 50%;
    background: var(--brand-green);
  }
  .brand-name {
    color: var(--brand-green);
    font-size: 34px;
    letter-spacing: 1px;
    text-transform: uppercase;
  }
  .front-contact {
    position: absolute;
    left: 60px;
    top: 200px;
  }
  .dentist-name {
    color: var(--brand-green);
    font-size: 36px;
    margin-bottom: 10px;
  }
  .dentist-phone {
    color: var(--text-grey);
    font-size: 38px;
    letter-spacing: 1px;
  }
  /* Back */
  .card-back {
    top: 618px;
    background: var(--card-white);
    overflow: hidden;
  }
  .back-band {
    position: absolute;
    top: 0; left: 0; right: 0;
    height: 44px;
    background: var(--card-black);
  }
  .back-title {
    position: absolute;
    right: 60px;
    top: 62px;
    color: var(--brand-green);
    font-family: "Montserrat", sans-serif;
    font-weight: 600;
    font-size: 28px;
    letter-spacing: 1px;
    text-transform: uppercase;
  }
  .appointment-fields {
    position: absolute;
    left: 50px;
    right: 50px;
    top: 120px;
  }
  .field {
    position: relative;
    height: 62px;
    border-bottom: 1px solid var(--rule);
    font-size: 22px;
    color: var(--ink);
  }
  .field-label {
    position: absolute;
    bottom: 6px;
  }
  .field-label.time { left: 470px; }
  .practice-details {
    position: absolute;
    left: 50px;
    bottom: 70px;
    color: var(--ink);
    font-size: 22px;
    line-height: 1.45;
  }
  .practice-web {
    font-family: "Montserrat", sans-serif;
    font-weight: 600;
    font-size: 24px;
  }
</style>
</head>
<body>
  <section class="card card-front" aria-label="Business card front">
    <div class="front-brand">
      <span class="brand-dot"></span>
      <span class="brand-name">Harbourlight Dental Centre</span>
    </div>
    <div class="front-contact">
      <p class="dentist-name">Dr. Raj Kalpat</p>
      <p class="dentist-phone">07- 5918 2243</p>
    </div>
  </section>

  <section class="card card-back" aria-label="Business card back – appointment">
    <div class="back-band"></div>
    <h2 class="back-title">Appointment</h2>
    <div class="appointment-fields">
      <div class="field"><span class="field-label">For</span></div>
      <div class="field">
        <span class="field-label">Date</span>
        <span class="field-label time">Time</span>
      </div>
    </div>
    <address class="practice-details" style="font-style: normal;">
      <p>117C, 58 Tarrow Street, Kelvale - 4561, Queensland</p>
      <p>admin@harbourlightdentalkelvale.example.au</p>
      <p class="practice-web">www.harbourlightdental.example.au</p>
    </address>
  </section>
</body>
</html>
```